Homvuk Business Card Project showing the logo and a bellan image on the rear

Design a whacky but professional business card, the logo is for the front and the Bellan image is for the rear. Happy to consider other open source Bellan Images if the designer wants to select one from the web. Homvuk is a competitor to TKU.com.au and Parcelo.com.au and is based around every property in Australia

Target Market(s)

Business

Contact Information for Business Card

Name, Title, Email, Web, Phone Number

Font styles to use
Other font styles liked:
• avenir

Requirements
Must have
• Image on Back logo on front
Nice to have
• Happy to consider other images on rear, preftably Oskar Bellan. Image supplied I own, we can use open source other Bellan Images

```html
<!DOCTYPE html>
<html lang="en">
<head>
<meta charset="utf-8">
<title>Homvuk Business Card</title>
<link rel="stylesheet" href="https://fonts.googleapis.com/css2?family=Nunito+Sans:wght@400;600;800&display=swap">
<style>
  :root {
    --stage: #e9e4dc;
    --card: #ffffff;
    --orange: #f7941d;
    --ink: #1d1d1d;
    --muted: #2a2a2a;
    --night: #2b3f9e;
    --sky: #5a8fd8;
    --dusk: #7b4fb0;
    --brick: #d9534f;
    --lime: #8cc63f;
  }
  * { box-sizing: border-box; margin: 0; padding: 0; }
  html, body { width: 900px; height: 1200px; overflow: hidden; }
  body {
    background: var(--stage);
    font-family: "Nunito Sans", "Avenir", sans-serif;
    color: var(--ink);
    position: relative;
  }
  .card {
    position: absolute;
    left: 84px;
    width: 732px;
    height: 500px;
    border-radius: 22px;
    overflow: hidden;
    box-shadow: 0 10px 28px rgba(0,0,0,0.25);
  }
  .card-front { top: 110px; background: var(--card); }
  .card-back { top: 650px; }
  .card-shapes { position: absolute; inset: 0; width: 100%; height: 100%; }
  .contact-block {
    position: absolute;
    left: 372px;
    top: 110px;
  }
  .person-name { font-size: 36px; font-weight: 800; line-height: 1.1; }
  .person-title { font-size: 20px; font-weight: 400; color: var(--muted); margin-top: 4px; }
  .contact-list {
    list-style: none;
    position: absolute;
    left: 372px;
    top: 200px;
    font-size: 17px;
    color: var(--muted);
  }
  .contact-list li { display: flex; align-items: center; gap: 12px; margin-bottom: 8px; }
  .contact-icon { width: 15px; height: 15px; fill: var(--ink); flex: none; }
  .brand {
    position: absolute;
    left: 48px;
    top: 362px;
    display: flex;
    align-items: center;
    gap: 14px;
  }
  .brand-mark { width: 50px; height: 50px; background: var(--orange); border-radius: 6px; }
  .brand-name { font-size: 54px; font-weight: 800; color: var(--ink); letter-spacing: 0.5px; line-height: 1; }
  .artwork {
    position: absolute;
    inset: 0;
    background:
      linear-gradient(180deg, rgba(43,63,158,0) 45%, rgba(0,0,0,0.05) 100%),
      linear-gradient(100deg, var(--sky) 0%, var(--dusk) 45%, var(--night) 70%, var(--night) 100%);
  }
  .artwork::after {
    content: "";
    position: absolute;
    left: 0; right: 0; bottom: 0;
    height: 62%;
    background: linear-gradient(90deg, var(--brick), var(--orange) 30%, var(--lime) 55%, var(--dusk) 80%, var(--brick));
    opacity: 0.75;
  }
</style>
</head>
<body>
  <section class="card card-front" aria-label="Business card front">
    <svg class="card-shapes" viewBox="0 0 732 500" aria-hidden="true">
      <polygon points="0,0 150,0 0,90" fill="var(--orange)"/>
      <polygon points="118,0 250,0 190,70" fill="var(--orange)"/>
      <polygon points="0,430 40,500 0,500" fill="var(--ink)"/>
      <polygon points="560,500 732,420 732,500" fill="var(--orange)"/>
      <polygon points="336,78 712,78 702,300 400,306 300,348 350,300 336,300" fill="var(--orange)"/>
    </svg>
    <div class="contact-block">
      <p class="person-name">Dale Varga</p>
      <p class="person-title">CEO/Founder</p>
    </div>
    <ul class="contact-list">
      <li><svg class="contact-icon" viewBox="0 0 16 16"><path d="M3 1l3 3-2 2c1 2 3 4 5 5l2-2 3 3-2 3C7 14 2 9 1 3z"/></svg>214-555-0188</li>
      <li><svg class="contact-icon" viewBox="0 0 16 16"><rect x="1" y="3" width="14" height="10" rx="1"/><path d="M1 3l7 6 7-6" fill="none" stroke="#f7941d" stroke-width="1.4"/></svg>Dale@Homvuk.com</li>
      <li><svg class="contact-icon" viewBox="0 0 16 16"><circle cx="8" cy="8" r="7"/></svg>www.yourwebsitehere.com</li>
    </ul>
    <div class="brand">
      <span class="brand-mark"></span>
      <span class="brand-name">Homvuk</span>
    </div>
  </section>

  <section class="card card-back" aria-label="Business card back">
    <div class="artwork" role="img" aria-label="Colourful pop-art illustration of a city skyline with cheerful buildings, a sun and clouds by day on the left and a starry night sky with a moon on the right"></div>
  </section>
</body>
</html>
```